San Antonio Texas Based Law Firm Needs Eye Catching Professional website

The Wrenfield Law Firm, PLLC is in need of a fresh, eye catching website that makes the small firm look and appear as professional, organized and innovative as possible.

The Firm wants to highlight its expertise in three main areas.
Estate Planning, Insurance and Mediation.

It is a small firm - but growing, so I am looking for the website to have the appearance not of a small firm - but more of the appearance of a leading national firm. The firm was built after obtaining extensive experience working in both private practice and at two Summit 400 companies.

The firm was formed based on strong relationships and reputation in the industries the Firm serves and and in the local communities.

My logo, which was designed by pixel forge is clever and something I want to make prominent and build from.

Industry/Entity Type

Legal

Coding

Coded - Design and coding required

Number of Pages Required

3 page

Colors
ffffff
000000

Requirements
Must have
• Very good quality pictures.
• Very organized.
• Easy to navigate.
• A contact Us Page.
• On the Estate Planning page, a place for an upcoming seminar sign up - where we
• would get potential client information to mail out confirmation.
• A way to have people subscribe to periodic updates.
• Link to The Wrenfield Law Firm Chatterly
• A way to download vcard.
Should not have
• Any pictures of gavels, pillars or other common pictures related to law. (Too boring)

```html
<!DOCTYPE html>
<html lang="en">
<head>
<meta charset="utf-8">
<title>The Wrenfield Law Firm, PLLC</title>
<link href="https://fonts.googleapis.com/css2?family=Bree+Serif&family=Open+Sans:ital,wght@0,400;0,600;0,700;1,400&family=Play:wght@400;700&display=swap" rel="stylesheet">
<style>
:root{
  --black:#000;
  --ink:#1e1e1e;
  --dark:#2b2b2b;
  --footer:#232323;
  --white:#fff;
  --paper:#f2f2f2;
  --grey:#8a8a8a;
  --muted:#9a9a9a;
  --field:#4a4a4a;
  --rule:#3c3c3c;
}
*{box-sizing:border-box;margin:0;padding:0}
html,body{width:1200px;height:3564px;overflow:hidden}
body{font-family:"Open Sans",Arial,sans-serif;color:var(--ink);background:var(--white);position:relative}
.section{position:absolute;left:0;width:1200px}
.photo{position:absolute;display:block}

/* header */
.site-header{top:0;height:143px;background:var(--black);color:var(--white)}
.brand{position:absolute;left:100px;top:30px;display:flex;flex-direction:column;align-items:center;gap:10px}
.brand-square{width:44px;height:44px;border:2px solid var(--white)}
.brand-name{font-family:"Open Sans",sans-serif;font-size:13px;letter-spacing:1px;text-transform:uppercase;font-weight:400}
.main-nav{position:absolute;right:105px;top:62px;display:flex;gap:31px;font-size:14px;text-transform:uppercase}

/* hero */
.hero{top:143px;height:522px;background:linear-gradient(120deg,#3a3a3a 0%,#6e6e6e 45%,#262626 100%);color:var(--white);text-align:center}
.hero h1{position:absolute;top:140px;width:100%;font-family:"Bree Serif",serif;font-weight:400;font-size:42px}
.hero p{position:absolute;top:220px;left:380px;width:460px;font-size:19px;line-height:26px}
.btn-vcard{position:absolute;left:490px;top:332px;width:265px;height:60px;background:var(--white);color:var(--black);font-weight:700;font-size:16px;line-height:60px;text-transform:uppercase}

/* services */
.services{top:665px;height:447px}
.service{position:absolute;top:76px;width:268px;text-align:center}
.service .photo{position:relative;width:268px;height:179px;border-radius:26px}
.service h3{font-size:16px;font-weight:400;margin-top:26px;color:var(--ink)}
.service p{font-size:11.5px;color:var(--muted);line-height:19px;margin-top:12px}

/* seminar */
.seminar{top:1112px;height:551px;background:linear-gradient(180deg,#cfe0e6 0%,#a9b6bd 40%,#2c3036 100%)}
.seminar-box{position:absolute;left:261px;top:266px;width:661px;height:285px;background:rgba(255,255,255,.86);text-align:center}
.seminar-box h2{font-family:"Play",sans-serif;font-weight:400;font-size:36px;color:var(--ink);margin-top:18px}
.field{display:block;margin:0 auto;width:412px;height:38px;background:var(--field);color:var(--white);font-size:14px;line-height:38px;text-align:left;padding-left:20px}
.field.first{margin-top:22px}.field+.field{margin-top:14px}
.btn-submit{display:inline-block;margin-top:22px;width:130px;height:44px;border:2px solid var(--black);font-weight:700;font-size:14px;line-height:40px}

/* story */
.story{top:1663px;height:511px}
.section-title{position:absolute;top:44px;width:100%;text-align:center;font-family:"Play",sans-serif;font-weight:400;font-size:38px}
.story-media{position:absolute;left:150px;top:124px;width:373px;height:311px;background:var(--ink)}
.story-media .photo{width:373px;height:240px}
.story-media figcaption{color:var(--white);font-style:italic;font-size:12px;text-align:center;line-height:20px;padding:12px 30px}
.story-text{position:absolute;left:570px;top:100px;width:548px;font-size:11.5px;line-height:19px;color:#555}
.story-text p+p{margin-top:14px}

/* testimonials */
.testimonials{top:2174px;height:487px;background:var(--dark);color:var(--white)}
.testimonials .section-title{top:56px}
.quote{position:absolute;top:202px;width:316px;height:214px;background:var(--paper);color:var(--ink);text-align:center;padding-top:70px}
.avatar{position:absolute;top:-42px;left:118px;width:80px;height:80px;border-radius:50%;border:4px solid var(--white)}
.quote h4{font-size:13px;font-weight:700;text-transform:uppercase}
.quote .role{font-size:11px;font-style:italic;color:var(--grey);margin-top:8px}
.quote blockquote{font-size:11.5px;font-style:italic;line-height:19px;margin:16px 30px 0}

/* news */
.news{top:2661px;height:575px}
.news .section-title{top:46px}
.post{position:absolute;top:133px;width:311px}
.post .photo{position:relative;width:311px;height:212px}
.date{position:absolute;right:0;bottom:0;background:var(--black);color:var(--white);font-size:10px;font-weight:700;padding:8px 12px}
.post h3{font-size:14px;font-weight:700;margin-top:22px}
.post p{font-size:11.5px;line-height:18px;color:#555;margin-top:14px}
.read-more{display:block;font-size:10px;font-weight:700;text-transform:uppercase;margin-top:16px}

/* footer */
.site-footer{top:3236px;height:328px;background:var(--footer);color:var(--white)}
.site-footer .brand{left:120px;top:28px}
.site-footer .brand-square{width:40px;height:40px}
.site-footer .brand-name{font-size:11px}
.social{position:absolute;right:110px;top:42px;display:flex;gap:20px;font-size:13px}
.social span{display:flex;align-items:center;gap:6px}
.social i{width:8px;height:8px;background:var(--white);display:inline-block}
.footer-rule{position:absolute;left:40px;right:40px;top:118px;border-top:1px solid var(--rule)}
.contact-item{position:absolute;top:162px;display:flex;gap:16px;align-items:center;font-size:11.5px;line-height:17px;color:#bdbdbd}
.copyright{position:absolute;top:272px;width:100%;text-align:center;font-size:11px;color:#9d9d9d}
</style>
</head>
<body>

<header class="section site-header">
  <div class="brand"><span class="brand-square"></span><span class="brand-name">The Wrenfield Law Firm, PLLC</span></div>
  <nav class="main-nav"><span>Home</span><span>About</span><span>Services</span><span>Team</span><span>Clients</span><span>Contact</span></nav>
</header>

<section class="section hero" role="img" aria-label="Black and white photo of a lawyer signing documents at a desk">
  <h1>Let Our Experience be Your Guide.</h1>
  <p>Lorem ipsum dolor sit amet, consectetuer adipiscing elit, sed diam nonummy nibh euismod tincidunt ut laoreet dolore magna aliquam erat volutpat.</p>
  <span class="btn-vcard">Download our vCard</span>
</section>

<section class="section services">
  <article class="service" style="left:138px">
    <div class="photo" role="img" aria-label="Family meeting with an advisor at home" style="background:linear-gradient(135deg,#b48463,#e6d4c4)"></div>
    <h3>Estate Planning</h3>
    <p>Fusce commodo eros quis molestie blandit. Aliquam sollicitudin maximus metus ac ullamcorper. Fusce commodo eros quis molestie blandit.</p>
  </article>
  <article class="service" style="left:463px">
    <div class="photo" role="img" aria-label="Couple reviewing an insurance plan with an agent" style="background:linear-gradient(135deg,#6f8fb0,#e2d2c2)"></div>
    <h3>Insurance</h3>
    <p>Fusce commodo eros quis molestie blandit. Aliquam sollicitudin maximus metus ac ullamcorper. Fusce commodo eros quis molestie blandit.</p>
  </article>
  <article class="service" style="left:791px">
    <div class="photo" role="img" aria-label="Business handshake across a table" style="background:linear-gradient(135deg,#c8c8c8,#8d8a86)"></div>
    <h3>Mediation</h3>
    <p>Fusce commodo eros quis molestie blandit. Aliquam sollicitudin maximus metus ac ullamcorper. Fusce commodo eros quis molestie blandit.</p>
  </article>
</section>

<section class="section seminar" role="img" aria-label="Team of business professionals standing in an office">
  <form class="seminar-box">
    <h2>Signup for Seminar Updates</h2>
    <span class="field first">Enter First Name</span>
    <span class="field">Enter your Mail Address</span>
    <span class="btn-submit">SUBMIT</span>
  </form>
</section>

<section class="section story">
  <h2 class="section-title">Our Story</h2>
  <figure class="story-media">
    <div class="photo" role="img" aria-label="Two businessmen meeting at an office desk" style="background:linear-gradient(135deg,#dfe5e8,#9ba6ad)"></div>
    <figcaption>Fusce commodo eros quis molestie blandit. Aliquam sollicitudin maximus metus ac ullamcorper.</figcaption>
  </figure>
  <div class="story-text">
    <p>Lorem ipsum dolor sit amet, consectetuer adipiscing elit, sed diam nonummy nibh euismod tincidunt ut laoreet dolore magna aliquam erat volutpat. Ut wisi enim ad minim veniam, quis nostrud exerci tation ullamcorper suscipit lobortis nisl ut aliquip ex ea commodo consequat. Duis autem vel eum iriure dolor in hendrerit in vulputate velit esse molestie consequat.</p>
    <p>" Nam liber tempor cum soluta nobis eleifend option congue nihil imperdiet doming id quod mazim placerat facer possim assum. Typi non habent claritatem insitam; est usus legentis in iis qui facit eorum claritatem."</p>
    <p>Mirum est notare quam littera gothica, quam nunc putamus parum claram, anteposuerit litterarum formas humanitatis per seacula quarta decima et quinta decima. Eodem modo typi, qui nunc nobis videntur parum clari, fiant sollemnes in futurum.</p>
  </div>
</section>

<section class="section testimonials">
  <h2 class="section-title">What Our Client Say</h2>
  <article class="quote" style="left:95px">
    <div class="avatar" role="img" aria-label="Client portrait" style="background:#9a9a9a"></div>
    <h4>Talia Brenner</h4><p class="role">Co. Founder at Nestwell</p>
    <blockquote>"We know that sometimes it's difficult to get to the phone if you are in the middle of something and you don't want to miss."</blockquote>
  </article>
  <article class="quote" style="left:440px">
    <div class="avatar" role="img" aria-label="Client portrait" style="background:#a08478"></div>
    <h4>Rosa Kinley</h4><p class="role">Co. Founder at Nestwell</p>
    <blockquote>"We know that sometimes it's difficult to get to the phone if you are in the middle of something and you don't want to miss."</blockquote>
  </article>
  <article class="quote" style="left:782px">
    <div class="avatar" role="img" aria-label="Client portrait" style="background:#b09080"></div>
    <h4>Owen Delray</h4><p class="role">Co. Founder at Nestwell</p>
    <blockquote>"We know that sometimes it's difficult to get to the phone if you are in the middle of something and you don't want to miss."</blockquote>
  </article>
</section>

<section class="section news">
  <h2 class="section-title">Latest News</h2>
  <article class="post" style="left:107px">
    <div class="photo" role="img" aria-label="Hands reviewing financial documents" style="background:linear-gradient(135deg,#eef0f2,#8c96a4)"><span class="date">Apr 10, 2016</span></div>
    <h3>The Bond Market Is Going</h3>
    <p>Find out your risk factor. Run our complimentary Intelligent Security Scan on your computer systems to see your security liability of having Personal Health Information.</p>
    <span class="read-more">Read More &gt;</span>
  </article>
  <article class="post" style="left:443px">
    <div class="photo" role="img" aria-label="Colleagues discussing work in an office" style="background:linear-gradient(135deg,#c7b7a8,#5b5e66)"><span class="date">May 25, 2016</span></div>
    <h3>To Get Ugly ITher Rebound Soon</h3>
    <p>Find out your risk factor. Run our complimentary Intelligent Security Scan on your computer systems to see your security liability of having Personal Health Information.</p>
    <span class="read-more">Read More &gt;</span>
  </article>
  <article class="post" style="left:777px">
    <div class="photo" role="img" aria-label="Advisor consulting with a client" style="background:linear-gradient(135deg,#d9c2b0,#b9473f)"><span class="date">Apr 10, 2016</span></div>
    <h3>Europese economie klimt langzaam</h3>
    <p>Find out your risk factor. Run our complimentary Intelligent Security Scan on your computer systems to see your security liability of having Personal Health Information.</p>
    <span class="read-more">Read More &gt;</span>
  </article>
</section>

<footer class="section site-footer">
  <div class="brand"><span class="brand-square"></span><span class="brand-name">The Wrenfield Law Firm</span></div>
  <div class="social"><span><i></i>Chatterly</span><span>Chirper</span><span>Tumblet</span><span>Flickbox</span><span>Circleup</span><span>Feed</span></div>
  <div class="footer-rule"></div>
  <div class="contact-item" style="left:145px">
    <svg width="30" height="36" viewBox="0 0 30 36" fill="none" stroke="#cfcfcf" stroke-width="2"><path d="M15 33C15 33 5 20 5 13a10 10 0 0 1 20 0c0 7-10 20-10 20z"/><circle cx="15" cy="13" r="4"/></svg>
    <span>Marlow, TX 78990<br>214 Cedarvale Lane</span>
  </div>
  <div class="contact-item" style="left:478px">
    <svg width="30" height="36" viewBox="0 0 30 36" fill="none" stroke="#cfcfcf" stroke-width="2"><path d="M8 4h6l2 8-4 3c2 4 5 7 9 9l3-4 8 2v6c-14 2-26-10-24-24z" transform="translate(-2 2) scale(.9)"/></svg>
    <span>Feel Free to Call Us Now<br>(555) 014 2290</span>
  </div>
  <div class="contact-item" style="left:810px">
    <svg width="34" height="34" viewBox="0 0 34 34" fill="none" stroke="#cfcfcf" stroke-width="2"><rect x="3" y="6" width="28" height="25"/><path d="M3 13h28M10 3v6M24 3v6M9 19h4M15 19h4M21 19h4M9 25h4M15 25h4"/></svg>
    <span>Working Hours<br>Mon-Fri 9:00am - 4:00pm</span>
  </div>
  <p class="copyright">Copyright © 2016 . All rights reserved.</p>
</footer>

</body>
</html>
```